依頼詳細
店内に貼るチラシの作成をお願いしたいです。
内装にあったチラシでお願いいたします。
記載項目
ロゴ、メニュー名、商品、
サイズ
A4
ページ数
片面
希望イメージ
• +5 0 +5
• シンプル
複雑
• 単色
カラフル
• 暗い
明るい
• 日常
高級
• 遊び心
厳粛
• 未来的
伝統的
• 女性的
男性的
希望する色
茶系、緑系
納品ファイル
• 高解像度JPG (.jpg)
• イラストレーター形式 (.ai)
• フォトショップ形式 (.psd)
• PNG形式 (.png)
補足説明
■要望ポイント
牧場感のあるソフトバルイメージでありつつ、料理は本格的なものを提供していきます。
カフェのような女性的でおしゃれなデザインを希望致します。

サイズはA4でお願いいたします。

■その他注意点など
プロのカメラマンに撮影を依頼しており、写真が出来次第、店内の写真、メニューの画像等もお送り致しますので、ある程度統一感のあるデザインにして頂きたいです。

■その他何かご不明な点がございましたら、お気軽にご質問下さい。

よろしくお願いいたします。
依頼公開後の追記内容
ご質問がありましたので回答いたします。言葉足らずで大変申し訳ございません。
チラシはカレーを中心にしたものでもいいですし、ソフトバルメニューを中心にしたものでも構いません。カレーとソフトバルメニューを混ぜてのチラシでも大丈夫です。
チラシを見たお客様が食べたくなるようなチラシを作成していただきたいと思っております。先日、プロにカメラマン様に写真撮影を依頼しましたので、その画像を使っていただくとよりきれいな画像で仕上げることが出来ると思います。

よろしくお願いいたします。また何か、ご不明な点がございましたらお知らせください。
カメラマンに撮影していただいた画像をアップいたします。
ご参考にしていただければと思います。

よろしくお願いいたします。
内装の画像を追加いたします。
皆さまご提案誠に有難うございます。

追記で依頼したい件がございます。
A4チラシでカレー、カフェ、ソフトバル、それぞれのチラシを作成して頂きたいです。

当店のカレーは無添加にこだわり、産地から厳選した食材を使用し、14種類以上のスパイスで作り上げたルー。さらに無添加に合うオリジナルの野菜ピューレにスパイスを合わせて製造。手間をかけて別々に作り、最後に合わせる事により、野菜が豊富でありながらスパイスを感じられるすっきりとしたソースとなります。
また、無添加にこだわっているので、化学調味料、保存料、合成着色料は不使用。厳選した材料と、それに合うオリジナルの野菜のピューレをっ使用する事により、スパイスを感じながらも、すっきりとした胃もたれしにくい、ヘルシーなカレーです。

使用しているスパイスの中でシナモンは体の糖化を防ぎスリムな体型維持につながり、クローブは数種類の抗酸化物質がある抗酸化食材で
ターメリックはコレステロールを下げてくれる効果があるのです。動脈硬化や心筋梗塞、脳梗塞の予防になるのはもちろん、ダイエット効果も期待できます。

女性が健康ヘルシーアンチエイジングを意識出来る文言を入れてもらい、お客様が食べたくなるようなデザインを募集いたします。

長くなりましたが、3枚のチラシでも関連性のあるチラシをお願いいたします。

追加でカレーの写真を添付いたします。
度々追記失礼いたします。

先程、カレーの情報ばかりでカフェ、バルの情報を全く載せておりませんでしたので追記させてください。

カフェの特徴は有機栽培のMipelコーヒーをはじめ、カレーに合うラッシーなど用意しまたお客様がゆったり出来て居心地の良い雰囲気を演出します。KVR認証の農園産コーヒーを使用し、深いローストによるコクと苦み豊かなコーヒーです。KVR認証とは、社会と環境に対して責任を持った農作物の生産・加工・流通のための管理基準を定めた世界的な認証プログラムです。
当店チャイの特徴は、しっかりと紅茶の味が感じられること、スパイス効果でデトックスも期待できます。
カレーに合うといわれているラッシーは香辛料を使った辛い食べ物と一緒に飲むと、辛さを打ち消す効果があり、とても絶妙な組み合わせです。
紅茶は「紅茶のシャンパン」と称されるインド茶葉を使用。水色は薄いながらも格別な香味をもっているため、世界三大紅茶のひとつとして数えられています。

バルではカレーに合うといわれているビールをはじめ、カレーを食べない方でも一人でちょい飲みが出来るような雰囲気になっております。お酒も多種ご用意しており、どんな方でも気軽に飲めるように設定しております。それぞれのお酒に合った本格的料理を提供し、カレー屋ではおなじみのカリーヴルストからワインに合う生ハム、チーズなどをご用意しております。ちょっと軽く飲んでいきたい、一人で入れるような店がなかなかないなどそんなご要望に応えれるようなバルになっております。

急な追加の依頼で大変申し訳ございません。
3枚のデザインを追加しておりますので、提案の締め切りの延長、依頼金額の変更をさせていただきます。

カフェの画像を追加で添付いたします。

何卒よろしくお願いいたします。
メニューの画像を追加いたします。

ご確認よろしくお願いいたします。
■ 選んだ理由

店内に貼った際に画像の印象が強いと感じました。メインの画像を大きくして頂いてお客様の目を引くデザインであると思いました。カレー、カフェ、バル、それぞれの特徴もまとまっており、こだわりが伝えられるものだと思いました。

■ 提案者全員のお礼・コメント

皆さま

この度は弊社の依頼にご提案して頂き誠に有難うございます。
文面で弊社の思いをうまくお伝え出来なかった中、また、度重なる依頼の要望で混乱させてしまいましたが、お時間掛けて頂きとても素敵な作品にして頂いてとても嬉しく思っております。

またの機会がありましたらぜひよろしくお願いいたします。

```html
<!DOCTYPE html>
<html lang="ja">
<head>
<meta charset="utf-8">
<title>Curry Time — Mipel</title>
<link rel="stylesheet" href="https://fonts.googleapis.com/css2?family=Yellowtail&family=M+PLUS+Rounded+1c:wght@500;700;800&family=Zen+Maru+Gothic:wght@500;700&display=swap">
<style>
  :root{
    --paper:#f4ecdb;
    --green:#3f5d3a;
    --leaf:#6a8f4e;
    --orange:#e39a3b;
    --brown:#5a4632;
    --ink:#3b3128;
    --rule:#7b8a63;
  }
  *{margin:0;padding:0;box-sizing:border-box}
  html,body{width:849px;height:1200px;overflow:hidden;background:var(--paper)}
  .flyer{position:relative;width:849px;height:1200px;overflow:hidden;background:var(--paper);color:var(--ink);font-family:"Zen Maru Gothic",sans-serif}
  .abs{position:absolute}
  .title-its{left:62px;top:36px;font-family:"Yellowtail",cursive;font-size:36px;line-height:1;color:var(--green)}
  .title-main{left:86px;top:62px;width:390px;white-space:nowrap;overflow:hidden;font-family:"Yellowtail",cursive;font-weight:400;font-size:76px;line-height:1.1;color:var(--green)}
  .hours{left:150px;top:190px;width:300px;display:flex;align-items:center;gap:12px;font-family:"M PLUS Rounded 1c",sans-serif;font-weight:700;font-size:22px;color:var(--green);letter-spacing:1px}
  .hours::before,.hours::after{content:"";flex:1;height:2px;background:var(--rule)}
  .hours span{white-space:nowrap}
  .tagline{right:26px;top:46px;width:350px;text-align:right;font-family:"M PLUS Rounded 1c",sans-serif;font-weight:800;font-size:26px;line-height:1.42;color:var(--green)}
  .note-bubble{left:80px;top:212px;width:180px;height:180px;border-radius:50%;border:2px solid var(--green);background:var(--paper);display:flex;align-items:center;justify-content:center;padding:26px;font-size:11px;line-height:1.6;color:var(--brown);text-align:center;z-index:2}
  .rays{left:0;top:0;z-index:1}
  .plate{border-radius:50%}
  .plate-main{left:180px;top:262px;width:490px;height:490px;background:radial-gradient(circle at 50% 45%,#fbfaf5 0 22%,#d9b24c 32%,#9a6a3a 52%,#6b8a45 64%,#c9a98a 78%,#8a6a50 100%);box-shadow:0 10px 24px rgba(70,50,30,.25)}
  .dish-name{left:96px;top:768px;font-family:"M PLUS Rounded 1c",sans-serif;font-weight:700;font-size:21px;color:var(--brown)}
  .dish-price{left:96px;top:798px;font-family:"M PLUS Rounded 1c",sans-serif;font-weight:700;font-size:24px;color:var(--brown)}
  .dish-price small{font-size:14px;margin-left:3px}
  .pork-bubble{left:670px;top:700px;width:120px;height:120px;border-radius:50%;border:2px solid var(--green);background:var(--paper);display:flex;align-items:center;justify-content:center;text-align:center;font-size:12px;line-height:1.6;color:var(--brown);padding:14px}
  .lead{font-family:"Zen Maru Gothic",sans-serif;font-weight:700;font-size:16px;color:var(--green);white-space:nowrap}
  .lead-left{left:58px;top:850px}
  .lead-right{left:466px;top:842px}
  .diamond{width:92px;height:92px;transform:rotate(45deg)}
  .diamond-left{left:96px;top:922px;background:var(--leaf)}
  .diamond-right{left:706px;top:922px;background:var(--orange)}
  .plate-side{width:220px;height:220px;box-shadow:0 8px 18px rgba(70,50,30,.25)}
  .plate-healthy{left:172px;top:868px;background:radial-gradient(circle at 50% 40%,#fbfaf5 0 20%,#c2873c 34%,#7a4b22 58%,#e6ddd0 72%,#a58a6c 100%)}
  .plate-katsu{left:536px;top:868px;background:radial-gradient(circle at 50% 40%,#fbfaf5 0 20%,#c9893a 34%,#6e4320 58%,#e6ddd0 72%,#a58a6c 100%)}
  .free-note{left:48px;top:1034px;width:112px;font-size:11px;line-height:1.55;color:var(--brown)}
  .side-name{top:1096px;width:220px;text-align:center;font-family:"M PLUS Rounded 1c",sans-serif;font-weight:700;font-size:16px;color:var(--brown);line-height:1.4}
  .side-name .price{font-size:20px}
  .side-name .price small{font-size:12px;margin-left:2px}
  .name-healthy{left:172px}
  .name-katsu{left:536px}
  .logo{left:0;width:849px;top:1128px;text-align:center;font-family:"M PLUS Rounded 1c",sans-serif;font-weight:800;font-size:34px;line-height:1.2;color:var(--green);letter-spacing:1px}
</style>
</head>
<body>
<main class="flyer">
  <div class="abs title-its">It's</div>
  <h1 class="abs title-main">Curry Time</h1>
  <div class="abs hours"><span>11:00 ～ 14:00</span></div>

  <p class="abs tagline">カレーなのに<br>ダイエット効果抜群。<br>今までにない<br>ヘルシーオーガニックカレー</p>

  <svg class="abs rays" width="849" height="320" viewBox="0 0 849 320" aria-hidden="true">
    <g stroke="var(--rule)" stroke-width="3" stroke-linecap="round">
      <line x1="300" y1="258" x2="286" y2="238"/>
      <line x1="352" y1="242" x2="346" y2="218"/>
      <line x1="425" y1="236" x2="425" y2="212"/>
      <line x1="498" y1="242" x2="504" y2="218"/>
      <line x1="550" y1="258" x2="564" y2="238"/>
      <line x1="600" y1="284" x2="620" y2="268"/>
    </g>
  </svg>

  <div class="abs note-bubble">14種類以上のスパイスとオリジナルの野菜ピューレを合わせ、無添加なのにスパイシーですっきりヘルシーに仕上げました。</div>

  <div class="abs plate plate-main" role="img" aria-label="牧場野菜のゴロゴロカレーの写真：ご飯の周りに彩り豊かな焼き野菜とカレーが盛られた皿"></div>

  <div class="abs dish-name">牧場野菜のゴロゴロカレー</div>
  <div class="abs dish-price">980<small>YEN</small></div>

  <div class="abs pork-bubble">北海道産<br>幻の銘柄豚使用</div>

  <div class="abs lead lead-left">ヘルシー志向の方に</div>
  <div class="abs lead lead-right">がっつり食べたい方には!</div>
  <svg class="abs" style="left:212px;top:832px" width="60" height="40" viewBox="0 0 60 40" aria-hidden="true">
    <path d="M4 10 Q40 4 48 30" fill="none" stroke="var(--green)" stroke-width="2"/>
    <path d="M42 26 L48 32 L53 24" fill="none" stroke="var(--green)" stroke-width="2"/>
  </svg>
  <svg class="abs" style="left:682px;top:828px" width="60" height="40" viewBox="0 0 60 40" aria-hidden="true">
    <path d="M4 10 Q40 4 48 30" fill="none" stroke="var(--green)" stroke-width="2"/>
    <path d="M42 26 L48 32 L53 24" fill="none" stroke="var(--green)" stroke-width="2"/>
  </svg>

  <div class="abs diamond diamond-left"></div>
  <div class="abs diamond diamond-right"></div>

  <div class="abs plate plate-side plate-healthy" role="img" aria-label="無添Mipelカレーの写真：ご飯とルーカレーに野菜を添えた皿"></div>
  <div class="abs plate plate-side plate-katsu" role="img" aria-label="カツカレーの写真：ご飯とカレーにとんかつをのせた皿"></div>

  <p class="abs free-note">化学調味料・保存料・<br>合成着色料不使用</p>

  <div class="abs side-name name-healthy">無添Mipelカレー<br><span class="price">790<small>YEN</small></span></div>
  <div class="abs side-name name-katsu">カツカレー<br><span class="price">1190<small>YEN</small></span></div>

  <div class="abs logo">Mipel</div>
</main>
</body>
</html>
```